PELDRAX Business Cards

We require a business card for our company that provides IT consulting services. We already have a logo that needs to be used on the card. We want a clean professional looking design that incorporates our colours. Our main focus is providing managed services to business, which involves us looking after all of their IT requirements including managing servers/networks, projects, and procurement.

Industry/Entity Type

Information Technology

Requirements
Must have
• our logo, contact information, name, title, phone numbers

```html
<!DOCTYPE html>
<html lang="en">
<head>
<meta charset="utf-8">
<title>PELDRAX Business Cards</title>
<link href="https://fonts.googleapis.com/css2?family=Lato:wght@400;700&display=swap" rel="stylesheet">
<style>
  :root {
    --brand-blue: #0795cd;
    --page: #ffffff;
    --card-light: #fafbfb;
    --text-grey: #555a5e;
    --title-grey: #44484b;
    --card-edge: #e6e9eb;
  }
  html, body {
    margin: 0;
    padding: 0;
    width: 1200px;
    height: 1200px;
    overflow: hidden;
    background: var(--page);
    font-family: "Lato", sans-serif;
  }
  .canvas {
    position: relative;
    width: 1200px;
    height: 1200px;
  }
  .card {
    position: absolute;
    left: 246px;
    width: 708px;
    height: 404px;
    border-radius: 26px;
  }
  .card--front {
    top: 138px;
    background: var(--brand-blue);
  }
  .card--back {
    top: 646px;
    background: var(--card-light);
    border: 1px solid var(--card-edge);
    box-sizing: border-box;
  }
  .brand {
    position: absolute;
    display: flex;
    align-items: center;
    font-family: "Lato", sans-serif;
    font-weight: 700;
    line-height: 1;
  }
  .brand__mark {
    border-radius: 50%;
    flex: none;
  }
  .brand--front {
    left: 114px;
    top: 150px;
    color: #ffffff;
    font-size: 82px;
    letter-spacing: 4px;
    gap: 26px;
  }
  .brand--front .brand__mark {
    width: 96px;
    height: 96px;
    background: #ffffff;
  }
  .brand--back {
    left: 50px;
    top: 56px;
    color: var(--brand-blue);
    font-size: 50px;
    letter-spacing: 3px;
    gap: 18px;
  }
  .brand--back .brand__mark {
    width: 72px;
    height: 72px;
    background: var(--brand-blue);
  }
  .address {
    position: absolute;
    left: 47px;
    top: 208px;
    margin: 0;
    font-style: normal;
    font-size: 17px;
    line-height: 26px;
    color: var(--text-grey);
  }
  .contacts {
    position: absolute;
    left: 51px;
    top: 296px;
    margin: 0;
    padding: 0;
    list-style: none;
    font-size: 17px;
    line-height: 23.5px;
    color: var(--text-grey);
  }
  .contacts li {
    display: flex;
    align-items: center;
    gap: 12px;
  }
  .contacts svg {
    width: 11px;
    height: 11px;
    fill: var(--brand-blue);
    flex: none;
  }
  .contacts .accent {
    color: var(--brand-blue);
  }
  .person {
    position: absolute;
    right: 49px;
    top: 304px;
    text-align: right;
  }
  .person__name {
    margin: 0;
    font-size: 29px;
    font-weight: 700;
    color: var(--brand-blue);
    line-height: 34px;
  }
  .person__title {
    margin: 0;
    font-size: 17px;
    font-weight: 700;
    color: var(--title-grey);
    line-height: 22px;
  }
</style>
</head>
<body>
<main class="canvas">
  <section class="card card--front" aria-label="Business card front">
    <div class="brand brand--front">
      <span class="brand__mark" aria-hidden="true"></span>
      <span class="brand__name">PELDRAX</span>
    </div>
  </section>

  <section class="card card--back" aria-label="Business card back">
    <div class="brand brand--back">
      <span class="brand__mark" aria-hidden="true"></span>
      <span class="brand__name">PELDRAX</span>
    </div>

    <address class="address">
      Calle del Roble 14<br>
      Oficina 2B, 24010, León.
    </address>

    <ul class="contacts">
      <li>
        <svg viewBox="0 0 24 24" aria-hidden="true"><path d="M6.6 10.8c1.4 2.8 3.8 5.1 6.6 6.6l2.2-2.2c.3-.3.7-.4 1-.2 1.1.4 2.3.6 3.6.6.6 0 1 .4 1 1V20c0 .6-.4 1-1 1C10.6 21 3 13.4 3 4c0-.6.4-1 1-1h3.5c.6 0 1 .4 1 1 0 1.3.2 2.5.6 3.6.1.3 0 .7-.2 1l-2.3 2.2z"/></svg>
        <span>+34 900 412 368</span>
      </li>
      <li>
        <svg viewBox="0 0 24 24" aria-hidden="true"><path d="M2 5h20v14H2z M4 7v.4l8 5.2 8-5.2V7z" fill-rule="evenodd"/></svg>
        <span>info@peldrax.com</span>
      </li>
      <li>
        <svg viewBox="0 0 24 24" aria-hidden="true"><path d="M12 2a10 10 0 1 0 0 20 10 10 0 0 0 0-20zm0 2c.9 1.2 1.6 2.8 1.9 5h-3.8c.3-2.2 1-3.8 1.9-5zM4.3 13a8 8 0 0 1 0-2h3.8a19 19 0 0 0 0 2zm.6 2h3.5c.3 1.6.8 3 1.5 4.2A8 8 0 0 1 4.9 15zm3.5-6H4.9a8 8 0 0 1 5-4.2C9.2 6 8.7 7.4 8.4 9zM12 20c-.9-1.2-1.6-2.8-1.9-5h3.8c-.3 2.2-1 3.8-1.9 5zm2.1-7H9.9a17 17 0 0 1 0-2h4.2a17 17 0 0 1 0 2zm0 6.2c.7-1.2 1.2-2.6 1.5-4.2h3.5a8 8 0 0 1-5 4.2zm1.8-6.2a19 19 0 0 0 0-2h3.8a8 8 0 0 1 0 2zm-.3-4c-.3-1.6-.8-3-1.5-4.2a8 8 0 0 1 5 4.2z"/></svg>
        <span>www.<span class="accent">peldrax</span>.com</span>
      </li>
    </ul>

    <div class="person">
      <p class="person__name">Marcus Hale</p>
      <p class="person__title">Manager</p>
    </div>
  </section>
</main>
</body>
</html>
```